Brochure for financial planning firm

I need a brochure designed that will be folded into three panels idealy. I will provide the copy, logo, and some of the pictures.

Our primary business is finding investors for large-scale real estate developments.

Some of the pictures will have to come from outside this website given the file sizes. Please click the following link to download pictures of projects we have raised money for:

https://files.plorvex.net/share/7Qm2KtLw9ZxR4nVbY8HcPdJ3sFgT

Target Market(s)

People Ages 30 to 75. That are unsatisfied with their retirement investments

Industry/Entity Type

Financial

Requirements
Must have
• Addition to copy:
• To recieve information on our latest investments visit www.growsteadyfunds.ca
• Contact info:
• Torvanek Wealth Management Inc.
• 7 Orchard St. W.
• Suite K240
• Hamilton, ON L2P 5R8
• Office: (905) 634-2918
• www.torvanekwm.com
• The brochure must have somewhere printed on it near our contact info: RBTQ Lic # 40561

```html
<!DOCTYPE html>
<html lang="en">
<head>
<meta charset="utf-8">
<title>Syndicated Mortgages Brochure – Inside Spread</title>
<link href="https://fonts.googleapis.com/css2?family=Cabin:ital,wght@0,400;0,500;1,400&display=swap" rel="stylesheet">
<style>
  :root {
    --teal: #3fb8a5;
    --teal-soft: rgba(63, 184, 165, 0.9);
    --paper: #f4f5f5;
    --ink: #4a4f52;
    --white: #ffffff;
    --backdrop: #d9d9d9;
  }
  * { box-sizing: border-box; margin: 0; padding: 0; }
  html, body {
    width: 1200px; height: 800px; overflow: hidden;
    background: var(--backdrop);
    font-family: "Cabin", sans-serif;
  }
  .spread {
    position: absolute; left: 75px; top: 60px;
    width: 1050px; height: 680px;
    display: flex;
    box-shadow: 0 10px 30px rgba(0,0,0,0.18);
  }
  .panel { position: relative; width: 350px; height: 680px; overflow: hidden; }

  /* Left panel */
  .panel--intro { background: var(--paper); }
  .intro-photo {
    position: absolute; inset: 0;
    background: linear-gradient(180deg, #e6e6e6 0%, #a9a6a3 45%, #6d6a68 75%, #8c8884 100%);
  }
  .intro-box {
    position: absolute; left: 24px; top: 0; width: 290px; height: 300px;
    background: var(--teal-soft); color: var(--white);
    padding: 34px 24px 0;
  }
  .intro-title {
    font-weight: 400; font-size: 20px; line-height: 1.2;
    text-align: center; text-transform: uppercase; letter-spacing: 0.5px;
    margin-bottom: 16px;
  }
  .intro-text { font-size: 13.5px; line-height: 1.45; text-align: justify; }

  /* Middle panel */
  .panel--explain { background: var(--teal); color: var(--white); padding: 40px 34px 0; }
  .explain-title {
    font-weight: 400; font-size: 20px; text-transform: uppercase;
    text-align: center; letter-spacing: 0.5px;
  }
  .rule { height: 1px; background: var(--white); width: 230px; margin: 12px auto 22px; }
  .explain-text { font-size: 13.5px; line-height: 1.4; text-align: justify; margin-bottom: 14px; }
  .quote { font-size: 13px; line-height: 1.4; font-style: italic; text-align: justify; }

  /* Right panel */
  .panel--reasons { background: var(--paper); color: var(--ink); }
  .reasons-photo {
    position: absolute; left: 0; top: 0; width: 350px; height: 300px;
    background: linear-gradient(180deg, #2f63b8 0%, #6d93cf 35%, #8a5a4a 60%, #3b2f2c 100%);
  }
  .reasons-lead {
    position: absolute; left: 0; top: 210px; width: 350px; height: 90px;
    background: linear-gradient(180deg, rgba(0,0,0,0.35), rgba(0,0,0,0.8));
    color: var(--white); font-size: 13px; line-height: 1.35;
    padding: 12px 24px; text-align: justify;
  }
  .reasons-list { position: absolute; left: 0; top: 322px; width: 350px; padding: 0 24px; list-style: none; }
  .reason { display: flex; gap: 14px; margin-bottom: 22px; font-size: 13px; line-height: 1.4; }
  .reason-num {
    flex: 0 0 24px; height: 24px; margin-top: 18px;
    background: var(--teal); color: var(--white);
    font-size: 12px; display: flex; align-items: center; justify-content: center;
  }
  .reason-text { text-align: justify; }
</style>
</head>
<body>
<main class="spread">
  <section class="panel panel--intro">
    <div class="intro-photo" role="img" aria-label="Black and white photo of downtown condominium towers"></div>
    <div class="intro-box">
      <h2 class="intro-title">Use your RRSP to<br>invest in real estate</h2>
      <p class="intro-text">If you have ever looked at your RRSP statement and wondered if there was something other than the stocks, bonds or mutual funds your banker or financial advisor have told you are your best choices to grow your investments, well…there are. They are SYNDICATED MORTGAGES!</p>
    </div>
  </section>

  <section class="panel panel--explain">
    <h2 class="explain-title">Syndicated Mortgages</h2>
    <div class="rule"></div>
    <p class="explain-text">The simplest way to describe a syndicated mortgage is that it is a mortgage where two or more people loan their money in the form of one mortgage to another party.</p>
    <p class="explain-text">As a syndicated mortgage investor you become the bank! In other words, when you invest in a syndicated mortgage offered by Torvanek Wealth Management you are lending your money to a reputable real estate developer for a set interest rate.</p>
    <p class="explain-text">You might be thinking that lending mortgages are only for people with really deep pockets but in fact, if you have even $25,000 sitting in an account a mortgage investment is something you could take advantage of.</p>
    <p class="explain-text">RRSP, TFSA, RRIF, LIRA’s, and LIF’s are only some of the account types that are eligible for syndicated mortgage investments.</p>
    <div class="rule"></div>
    <p class="quote">“Mortgage investments are quickly changing retirement portfolios. People are tired of not having control over their money. The uncertainty of the markets keeps people up at night. As a financial planner mortgage investments give my clients and I a more stable position to plan their financial lives from.” – Daniel M. Ferreira, Principal Broker at Torvanek Wealth Management</p>
  </section>

  <section class="panel panel--reasons">
    <div class="reasons-photo" role="img" aria-label="Photo of a modern brick mid-rise condominium under a blue sky"></div>
    <p class="reasons-lead">There are many reasons why banks use mortgages as their preferred investments, here are just a few of those reasons and why you might want to think about adding a syndicated mortgage investment to your portfolio:</p>
    <ol class="reasons-list">
      <li class="reason"><span class="reason-num">1</span><span class="reason-text">Security of principle: Your investment is registered against physical real estate at the Land Registry Office. This doesn’t mean it’s a guaranteed investment, but it definitely reduces the risk of loss! No mutual fund or stock portfolio can do that.</span></li>
      <li class="reason"><span class="reason-num">2</span><span class="reason-text">A predictable rate of return: With a syndicated mortgage investment you know exactly what you are entitled to earn from your investment because your rate of interest is written right into your contract with the borrower. No more ups and downs of the stock market.</span></li>
      <li class="reason"><span class="reason-num">3</span><span class="reason-text">Term investment periods: A syndicated mortgage investment can range between a few months to about five years, depending on the project being built.</span></li>
    </ol>
  </section>
</main>
</body>
</html>
```